Kestly HVAC Services - High end letter head, Quote Template & Invoice Template

Provide word documents for the below.
- Letterhead for emails & letters.
- Quote template (similar to the attached)
- Invoice template (similar to the attached)
Logo colours should be used.
Modern, bold, professional look.
Kestly Logo - Voruma Specialist Dealer logo - Contact information

See attachments of previously used documents.

Target Market(s)

High end clients

Industry/Entity Type

Air Conditioning & Mechanical Ventilation (HVAC)

Font styles to use
Sans Serif
Other font styles liked:
• Arial Narrow or similar - Text similar to the KESTLY logo

Requirements
Must have
• Kestly Logo - Voruma Specialist Dealer logo - Contact information
Nice to have
• Logo colours used throughout the documents
Should not have
• Bright colours, yellow, pink, green etc

```html
<!DOCTYPE html>
<html lang="en">
<head>
<meta charset="utf-8">
<title>Kestly HVAC Services – Letterhead</title>
<link rel="stylesheet" href="https://fonts.googleapis.com/css2?family=Arimo:wght@400;700&family=Archivo+Narrow:wght@700&family=PT+Sans:wght@400&display=swap">
<style>
  :root {
    --paper: #f5f4f2;
    --ink: #3a3a3a;
    --body-ink: #555555;
    --muted: #6a6a6a;
    --logo-black: #0d0d0d;
    --logo-white: #ffffff;
    --brand-blue: #1f6fb9;
    --dealer-blue: #1aa0d8;
    --rule: #8a8a8a;
  }
  * { margin: 0; padding: 0; box-sizing: border-box; }
  html, body { width: 912px; height: 1200px; overflow: hidden; background: var(--paper); }
  .letterhead { position: relative; width: 912px; height: 1200px; background: var(--paper); font-family: "Arimo", Arial, sans-serif; color: var(--ink); }

  .brand-block { position: absolute; left: 0; top: 20px; width: 400px; height: 88px; background: var(--logo-black); color: var(--logo-white); padding: 10px 0 0 78px; }
  .brand-mark { position: absolute; left: 30px; top: 22px; width: 34px; height: 34px; border-radius: 50%; background: var(--brand-blue); }
  .brand-name { font-family: "Archivo Narrow", "Arial Narrow", sans-serif; font-weight: 700; font-size: 36px; line-height: 36px; letter-spacing: 1px; }
  .brand-sub { font-family: "Archivo Narrow", "Arial Narrow", sans-serif; font-weight: 700; font-size: 12px; letter-spacing: 1px; margin-top: 1px; }
  .brand-tagline { position: absolute; left: 72px; bottom: 10px; font-family: "Arimo", Arial, sans-serif; font-size: 10px; letter-spacing: 1.3px; }

  .contact { position: absolute; left: 611px; top: 42px; list-style: none; font-family: "PT Sans", Arial, sans-serif; font-size: 18px; color: #222; }
  .contact li { display: flex; align-items: center; height: 21px; }
  .contact svg { width: 12px; height: 12px; margin-right: 7px; fill: var(--brand-blue); }

  .salutation { position: absolute; left: 92px; top: 294px; font-size: 25px; color: var(--ink); }
  .letter-body { position: absolute; left: 92px; top: 360px; width: 736px; font-size: 14px; line-height: 21.4px; color: var(--body-ink); text-align: justify; }
  .letter-body p { margin-bottom: 13px; }

  .sign-off { position: absolute; left: 92px; top: 812px; font-size: 14px; color: var(--body-ink); }
  .signature { position: absolute; left: 86px; top: 846px; width: 120px; height: 40px; background: linear-gradient(90deg, rgba(40,40,40,0.15), rgba(40,40,40,0.05)); border-radius: 20px; }
  .signer-name { position: absolute; left: 97px; top: 908px; font-size: 19px; color: var(--ink); }
  .signer-role { position: absolute; left: 97px; top: 936px; font-size: 15px; color: var(--muted); }

  .footer-rule { position: absolute; left: 92px; top: 1110px; width: 538px; height: 1px; background: var(--rule); }
  .registration { position: absolute; left: 94px; top: 1126px; font-family: "PT Sans", Arial, sans-serif; font-size: 13px; color: var(--muted); }
  .dealer { position: absolute; left: 647px; top: 1098px; color: var(--dealer-blue); }
  .dealer-row { display: flex; align-items: center; }
  .dealer-square { width: 20px; height: 20px; background: var(--dealer-blue); margin-right: 6px; }
  .dealer-name { font-family: "Arimo", Arial, sans-serif; font-weight: 700; font-size: 26px; line-height: 26px; color: var(--dealer-blue); }
  .dealer-label { font-size: 8px; font-weight: 700; letter-spacing: 0.8px; text-align: right; color: #1d3c6e; margin-top: 2px; }
</style>
</head>
<body>
<main class="letterhead">
  <header>
    <div class="brand-block">
      <span class="brand-mark"></span>
      <div class="brand-name">KESTLY</div>
      <div class="brand-sub">HVAC SERVICES PTY LTD.</div>
      <div class="brand-tagline">| HEATING | VENTILATION | AIR CONDITIONING |</div>
    </div>
    <ul class="contact">
      <li><svg viewBox="0 0 12 12"><path d="M2.5 0.5 L4.5 0.5 L5.2 3.2 L3.8 4.3 C4.5 5.9 6 7.4 7.7 8.2 L8.8 6.8 L11.5 7.5 L11.5 9.5 C11.5 10.6 10.6 11.5 9.5 11.5 C4.6 11.5 0.5 7.4 0.5 2.5 C0.5 1.4 1.4 0.5 2.5 0.5 Z"/></svg>0412 555 087</li>
      <li><svg viewBox="0 0 12 12"><path d="M0.5 2.5 H11.5 V10 H0.5 Z M1 3 L6 6.8 L11 3" stroke="#f5f4f2" stroke-width="0.9"/></svg>office@kestlyhvac.com.au</li>
      <li><svg viewBox="0 0 12 12"><circle cx="6" cy="6" r="5.5"/><path d="M0.5 6 H11.5 M6 0.5 C3.5 3 3.5 9 6 11.5 M6 0.5 C8.5 3 8.5 9 6 11.5" stroke="#f5f4f2" stroke-width="0.8" fill="none"/></svg>www.kestlyhvac.com.au</li>
    </ul>
  </header>

  <p class="salutation">Dear Mr. Harlow,</p>

  <section class="letter-body">
    <p>Lorem ipsum dolor sit amet, consectetur adipiscing elit. Donec orci purus, luctus vitae dignissim eu, iaculis sed purus. Vivamus faucibus, ipsum nec aliquet viverra, leo mauris condimentum ligula, sit amet sagittis enim ligula quis arcu. Nam egestas tortor id nisi porttitor mattis. In tortor ante, ultricies in suscipit a, tempus non massa. Vivamus et auctor mi. Fusce vel massa nulla. Phasellus nec eros mauris, et scelerisque orci.</p>
    <p>Donec malesuada orci vitae nulla accumsan porta a id massa. Quisque accumsan iaculis magna sit amet fringilla. Maecenas consequat, magna eget tincidunt semper, odio nibh rutrum mi, id feugiat ante nisi eu risus. Vestibulum nunc orci, rhoncus a placerat in, ultricies in mi. Cras mattis varius eros, vel fringilla nisi suscipit eget. Quisque scelerisque sagittis nulla at porttitor.</p>
    <p>Sed id augue vitae urna euismod commodo aliquet a quam. Pellentesque arcu velit, cursus et malesuada ut, consequat et diam. Nullam erat sem, rhoncus id ullamcorper vitae, rhoncus et arcu. In ultricies ultricies nulla, ut rutrum nisi iaculis at. Donec eu magna a metus ornare faucibus. Fusce aliquet faucibus ultricies. Morbi semper, est id tincidunt gravida, sem arcu adipiscing lacus, ac bibendum nulla leo eu purus. Quisque nec diam sed risus consectetur a ccumsan quis quis nibh. Vestibulum id purus lorem.</p>
    <p>It is a long established fact that a reader will be distracted by the readable content of a page when looking at its layout. The point of using Lorem Ipsum is that it has a more-or-less normal distribution of letters, as opposed to using 'Content here, content here', making it look like readable English. Many desktop publishing packages</p>
  </section>

  <p class="sign-off">Sincerely,</p>
  <div class="signature" role="img" aria-label="Handwritten signature of the sender"></div>
  <p class="signer-name">Evan Harlow</p>
  <p class="signer-role">CEO/ Founder</p>

  <footer>
    <div class="footer-rule"></div>
    <p class="registration">ABN: 57 604 223 918 | Licence No: 512846K | ARC No: AU73154</p>
    <div class="dealer">
      <div class="dealer-row"><span class="dealer-square"></span><span class="dealer-name">VORUMA</span></div>
      <div class="dealer-label">SPECIALIST DEALER</div>
    </div>
  </footer>
</main>
</body>
</html>
```